Anchored Rig Works Buisness card

We need to create a business card with the same theme you came up with for the truck. I have attached a picture of the truck for you to see. Also there is a picture of the logo as well as a sample business card that I really don't like.

Target Market(s)

Fleet service and heave equipment work

Industry/Entity Type

Fleet Service

Contact Information for Business Card

I have attached a sample card I want to make better. It has basic details on it.

Colors
0054AA
0677BA
7BADD7
CADEEF
E8F1F8
F0912C
F2A743
F7CA91
FBE8D2
FDF5EE

Requirements
Must have
• "Professional and clean, and I want to list some basic services. They include, "Mobile Hydraulics", Fleet Service, Computer diagnostics, "Roadside Service". I also want it to say "We come to you" and 24/7"
Nice to have
• Our Phone number is 1-888-514-2769

```html
<!DOCTYPE html>
<html lang="en">
<head>
<meta charset="utf-8">
<title>Anchored Rig Works – Business Card</title>
<link href="https://fonts.googleapis.com/css2?family=Arimo:wght@400;700&family=Archivo+Black&display=swap" rel="stylesheet">
<style>
  :root{
    --backdrop:#e8e8e6;
    --card:#2a2a2b;
    --card-edge:#232324;
    --gold:#e3a857;
    --text-grey:#9a9a9a;
    --text-light:#d9d9d9;
    --rule:#6e6e6e;
    --steel-dark:#303032;
    --steel-mid:#5a5a5c;
    --steel-light:#8a8a8c;
  }
  *{margin:0;padding:0;box-sizing:border-box}
  html,body{width:1200px;height:801px;overflow:hidden;background:var(--backdrop);font-family:"Arimo",Arial,sans-serif}
  .stage{position:relative;width:1200px;height:801px}
  .card{position:absolute;top:246px;width:540px;height:309px;background:var(--card);border:1px solid var(--card-edge);box-shadow:0 10px 24px rgba(0,0,0,.22);overflow:hidden}
  .card--front{left:40px}
  .card--back{left:620px}

  /* front */
  .brand{position:absolute;left:270px;top:28px;width:240px;height:104px}
  .brand__art{position:absolute;left:30px;right:0;top:0;height:64px;background:linear-gradient(160deg,var(--steel-light) 0%,var(--steel-mid) 55%,var(--card) 100%);opacity:.35;border-radius:4px}
  .brand__name{position:absolute;right:0;bottom:0;display:flex;align-items:center;gap:8px;white-space:nowrap;font-weight:700;font-size:19px;color:var(--gold);letter-spacing:.3px}
  .brand__mark{width:10px;height:10px;background:var(--gold)}
  .divider{position:absolute;left:40px;right:30px;top:196px;height:1px;background:var(--rule)}
  .person{position:absolute;left:40px;top:146px}
  .person__name{font-weight:700;font-size:23px;color:var(--gold);line-height:1.05}
  .person__title{font-size:13px;color:var(--text-grey);margin-top:3px}
  .address{position:absolute;right:30px;top:152px;text-align:right;font-size:12.5px;color:var(--text-grey);line-height:1.35}
  .contacts{position:absolute;left:40px;top:208px;list-style:none}
  .contacts li{display:flex;align-items:center;gap:9px;font-size:13px;color:var(--text-grey);height:22px}
  .contacts svg{width:13px;height:13px;flex:none}
  .contacts .accent{color:var(--gold)}

  /* back */
  .machine-art{position:absolute;left:0;top:0;width:540px;height:196px;background:linear-gradient(105deg,var(--steel-dark) 0%,var(--card) 35%,var(--steel-mid) 80%,var(--steel-light) 100%)}
  .services{position:absolute;left:40px;top:206px;right:30px}
  .services__heading{font-family:"Archivo Black","Arimo",sans-serif;font-size:16px;color:var(--gold);letter-spacing:1.5px;line-height:1.2}
  .services__list{list-style:none;margin-top:3px}
  .services__list li{font-size:13px;color:var(--text-light);letter-spacing:.6px;line-height:1.5;text-transform:uppercase;white-space:nowrap}
  .services__list .services__tagline{color:var(--gold);font-weight:700}
  .dot{display:inline-block;width:7px;height:7px;border-radius:50%;background:var(--gold);margin:0 7px 1px 0;vertical-align:middle}
  .dot--mid{margin-left:10px}
</style>
</head>
<body>
<main class="stage">
  <section class="card card--front" aria-label="Business card front">
    <div class="brand">
      <div class="brand__art" role="img" aria-label="Excavator arm emblem area"></div>
      <div class="brand__name"><span class="brand__mark"></span>Anchored Rig Works</div>
    </div>
    <div class="person">
      <p class="person__name">Daniel Porter</p>
      <p class="person__title">Manager</p>
    </div>
    <p class="address">4120 Harbor Mill Road<br>Lake Orrin Fl 34100</p>
    <div class="divider"></div>
    <ul class="contacts">
      <li><svg viewBox="0 0 16 16" aria-hidden="true"><path fill="#e3a857" d="M3.5 1.5l2.5 0 1 3.5-1.7 1.2a9 9 0 0 0 4.5 4.5L11 9l3.5 1v2.5c0 1-1 2-2 2A11 11 0 0 1 1.5 3.5c0-1 1-2 2-2z"/></svg>1-888-514-2769</li>
      <li><svg viewBox="0 0 16 16" aria-hidden="true"><rect x="1" y="3" width="14" height="10" fill="#e3a857"/><path d="M1 3l7 6 7-6" fill="none" stroke="#2a2a2b" stroke-width="1.4"/></svg>daniel@anchoredrigrentals.com</li>
      <li><svg viewBox="0 0 16 16" aria-hidden="true"><circle cx="8" cy="8" r="7" fill="#e3a857"/><path d="M1 8h14M8 1c-3 3.5-3 10.5 0 14M8 1c3 3.5 3 10.5 0 14" fill="none" stroke="#2a2a2b" stroke-width="1.1"/></svg><span>www.<span class="accent">anchoredrigrentals</span>.com</span></li>
    </ul>
  </section>

  <section class="card card--back" aria-label="Business card back">
    <div class="machine-art" role="img" aria-label="Large excavator arm and bucket illustration"></div>
    <div class="services">
      <h2 class="services__heading">SERVICES</h2>
      <ul class="services__list">
        <li><span class="dot"></span>Mobile Hydraulics<span class="dot dot--mid"></span>Fleet Service</li>
        <li><span class="dot"></span>Computer Diagnostics<span class="dot dot--mid"></span>Roadside Service</li>
        <li class="services__tagline"><span class="dot"></span>We come to you<span class="dot dot--mid"></span>24/7</li>
      </ul>
    </div>
  </section>
</main>
</body>
</html>
```